Keystone Prime Water Tank

I primarily market the water tanks so want a business care that reflects that. I have attached the water tank logo. You have been working on our water tank so maybe we can use that on the card et. I am leaving as one sided but can be double sided if that works. The information that needs to be on the cards is as follows: Gerald T. Munro Phone numbers: Office 555-284-9137 Direct 555-619-2405 Mobile 555-372-5841 email address: gerald@fieldgearworks.com Address P.O. Box 8273 Larkfield, GA 30512 Web Page: www.fieldgearworks.com. A lot to fit on the card. Thanks

```html
<!DOCTYPE html>
<html lang="en">
<head>
<meta charset="utf-8">
<title>Keystone Prime Water Tank – Business Card</title>
<link rel="stylesheet" href="https://fonts.googleapis.com/css2?family=Lato:wght@400;900&display=swap">
<style>
  :root {
    --page-bg: #e9e6e2;
    --card-black: #0d0d0d;
    --card-black-soft: #3a3a3a;
    --brand-red: #d3191c;
    --brand-red-deep: #b81316;
    --frost-light: #f1e6e4;
    --frost-pink: #d9a4a2;
    --text-light: #ececec;
    --text-dark: #111111;
  }
  * { margin: 0; padding: 0; box-sizing: border-box; }
  html, body { width: 1200px; height: 969px; overflow: hidden; background: var(--page-bg); }
  .canvas { position: relative; width: 1200px; height: 969px; }
  .business-card {
    position: absolute; left: 80px; top: 189px;
    width: 1040px; height: 591px;
    border-radius: 26px; overflow: hidden;
    box-shadow: 0 18px 40px rgba(0,0,0,.22);
    font-family: "Lato", sans-serif;
  }
  .card-shapes { position: absolute; inset: 0; width: 100%; height: 100%; display: block; }
  .holder-name {
    position: absolute; left: 59px; top: 62px;
    color: var(--brand-red); font-weight: 900; font-size: 37px; letter-spacing: .5px;
    line-height: 44px; text-transform: uppercase;
  }
  .contact-list {
    position: absolute; left: 59px; top: 116px; list-style: none;
    color: var(--text-light); font-size: 24px; font-weight: 400;
  }
  .contact-item { display: flex; align-items: flex-start; line-height: 29.5px; }
  .contact-item.address { margin-bottom: 5px; }
  .contact-icon { width: 22px; height: 22px; margin: 4px 14px 0 0; flex: none; fill: var(--brand-red); }
  .company-name {
    position: absolute; left: 492px; top: 432px; width: 440px;
    text-align: center; color: var(--text-dark);
    font-weight: 900; font-size: 34px; line-height: 38px; text-transform: uppercase;
  }
</style>
</head>
<body>
<div class="canvas">
  <div class="business-card">
    <svg class="card-shapes" viewBox="0 0 1083 616" preserveAspectRatio="none">
      <defs>
        <linearGradient id="blackPanel" x1="0" y1="0" x2="0.4" y2="1">
          <stop offset="0" stop-color="var(--card-black)"/>
          <stop offset="1" stop-color="var(--card-black-soft)"/>
        </linearGradient>
        <linearGradient id="frostPanel" x1="0" y1="0" x2="1" y2="1">
          <stop offset="0" stop-color="var(--frost-pink)"/>
          <stop offset=".5" stop-color="var(--frost-light)"/>
          <stop offset="1" stop-color="var(--frost-pink)"/>
        </linearGradient>
        <linearGradient id="redPanel" x1="0" y1="0" x2="1" y2="1">
          <stop offset="0" stop-color="var(--brand-red)"/>
          <stop offset="1" stop-color="var(--brand-red-deep)"/>
        </linearGradient>
      </defs>
      <rect class="frost-triangle" width="1083" height="616" fill="url(#frostPanel)" role="img" aria-label="Frosted triangle with faint stripe pattern from the water tank mark"/>
      <polygon class="black-panel" points="0,0 748,0 324,616 0,616" fill="url(#blackPanel)"/>
      <polygon class="red-corner" points="753,0 1083,0 1083,478" fill="url(#redPanel)"/>
    </svg>

    <h1 class="holder-name">Gerald T. Munro</h1>
    <ul class="contact-list">
      <li class="contact-item address">
        <svg class="contact-icon" viewBox="0 0 24 24"><path d="M12 2a7 7 0 0 0-7 7c0 5 7 13 7 13s7-8 7-13a7 7 0 0 0-7-7zm0 9.5A2.5 2.5 0 1 1 12 6.5a2.5 2.5 0 0 1 0 5z"/></svg>
        <span>P.O. Box 8273<br>Larkfield, GA 30512</span>
      </li>
      <li class="contact-item">
        <svg class="contact-icon" viewBox="0 0 24 24"><path d="M6.6 10.8a15 15 0 0 0 6.6 6.6l2.2-2.2a1 1 0 0 1 1-.25 11.4 11.4 0 0 0 3.6.6 1 1 0 0 1 1 1V20a1 1 0 0 1-1 1A17 17 0 0 1 3 4a1 1 0 0 1 1-1h3.5a1 1 0 0 1 1 1c0 1.25.2 2.45.6 3.6a1 1 0 0 1-.25 1z"/></svg>
        <span>555-284-9137</span>
      </li>
      <li class="contact-item">
        <svg class="contact-icon" viewBox="0 0 24 24"><path d="M6.6 10.8a15 15 0 0 0 6.6 6.6l2.2-2.2a1 1 0 0 1 1-.25 11.4 11.4 0 0 0 3.6.6 1 1 0 0 1 1 1V20a1 1 0 0 1-1 1A17 17 0 0 1 3 4a1 1 0 0 1 1-1h3.5a1 1 0 0 1 1 1c0 1.25.2 2.45.6 3.6a1 1 0 0 1-.25 1z"/></svg>
        <span>555-619-2405</span>
      </li>
      <li class="contact-item">
        <svg class="contact-icon" viewBox="0 0 24 24"><path d="M7 1h10a2 2 0 0 1 2 2v18a2 2 0 0 1-2 2H7a2 2 0 0 1-2-2V3a2 2 0 0 1 2-2zm0 3v14h10V4z"/></svg>
        <span>555-372-5841</span>
      </li>
      <li class="contact-item">
        <svg class="contact-icon" viewBox="0 0 24 24"><path d="M3 6h18v12H3zm2 2v.4l7 4.4 7-4.4V8l-7 4.4z"/></svg>
        <span>gerald@fieldgearworks.com</span>
      </li>
      <li class="contact-item">
        <svg class="contact-icon" viewBox="0 0 24 24"><circle cx="12" cy="12" r="9"/></svg>
        <span>fieldgearworks.com</span>
      </li>
    </ul>

    <p class="company-name">Keystone Prime<br>Water Tank</p>
  </div>
</div>
</body>
</html>
```